Commercial / Truck Battery Label

We need a high definition label design to send to a commercial printer for a Commercial/Truck Battery Label
I will upload our current truck battery label for you to get an idea of what we are looking for. Along with some competitor images and other logos for the label that we have on file. If we need to purchase a few images to make the label we can do that but need to see the design first.
The Labels need to have a plain white area which is 60mm Long x 40mm High along the bottom left corner. We will use this area for the battery specifications.
The Top Six Warning Icons downloaded also need to be on the label, perhaps along the bottom to the right of the white area in pairs. The icons size can be between 10mm x 10mm and 20mm x 20mm
The dimensions of the label need to be 390mm Long and the height needs to be both 140mm and 180mm. Same label 2 different sizes.
I would like to keep the terms : "SUPER HEAVY DUTY" and "THE STEADY CHARGE THAT HOLDS" on the label somewhere. Maybe replacing the word batteries or commercial with SUPER HEAVY DUTY under the right side of the VOLTMASTRO Logo.
The labels will be used predominantly on Black batteries, so a colour scheme or design to suit that.
I don't mind a completely fresh design or a reworking of the old design.
Look and feel
Each slider illustrates characteristics of the customer's brand and the style your logo design should communicate.

```html
<!DOCTYPE html>
<html lang="en">
<head>
<meta charset="utf-8">
<title>VOLTMASTRO Super Heavy Duty Battery Label</title>
<link href="https://fonts.googleapis.com/css2?family=Archivo+Black&family=Anton&family=Roboto:wght@400;700&family=Tinos&display=swap" rel="stylesheet">
<style>
  :root {
    --brand-blue: #0b3a84;
    --brand-red: #e3101d;
    --label-black: #111111;
    --panel-white: #ffffff;
    --page-bg: #ffffff;
    --ink: #1a1a1a;
  }
  html, body {
    margin: 0;
    width: 1198px;
    height: 1200px;
    overflow: hidden;
    background: var(--page-bg);
  }
  .battery-label {
    position: absolute;
    left: 85px;
    top: 415px;
    width: 1028px;
    height: 370px;
    box-shadow: 0 6px 14px rgba(0,0,0,0.35);
  }
  .brand-name { font-family: 'Archivo Black', sans-serif; fill: var(--brand-blue); }
  .product-name { font-family: 'Archivo Black', sans-serif; fill: var(--brand-blue); }
  .duty-line { font-family: 'Archivo Black', sans-serif; fill: var(--brand-blue); }
  .tagline { font-family: 'Anton', sans-serif; fill: var(--panel-white); }
  .spec-title { font-family: 'Anton', sans-serif; fill: var(--panel-white); font-size: 8px; }
  .spec-cell { font-family: 'Tinos', serif; fill: var(--ink); font-size: 7px; }
  .warning-text { font-family: 'Roboto', sans-serif; fill: var(--ink); font-size: 7px; }
  .warning-pb { font-family: 'Roboto', sans-serif; font-weight: 700; fill: var(--ink); }
</style>
</head>
<body>
<svg class="battery-label" viewBox="0 0 1028 370" xmlns="http://www.w3.org/2000/svg">
  <defs>
    <linearGradient id="hexFade" x1="0" y1="0" x2="1" y2="0">
      <stop offset="0" stop-color="#ffffff" stop-opacity="0"/>
      <stop offset="1" stop-color="#cfcfcf" stop-opacity="0.7"/>
    </linearGradient>
    <linearGradient id="redStripe" x1="0" y1="0" x2="1" y2="0">
      <stop offset="0" stop-color="var(--brand-red)"/>
      <stop offset="0.6" stop-color="#f08a90"/>
      <stop offset="1" stop-color="var(--brand-red)"/>
    </linearGradient>
  </defs>

  <!-- base panels -->
  <rect class="label-white" x="0" y="0" width="1028" height="370" fill="var(--panel-white)"/>
  <g role="img" aria-label="Faint honeycomb texture fading across the upper white area">
    <polygon points="380,0 1028,0 1028,40 823,40 742,232 380,232" fill="url(#hexFade)"/>
  </g>
  <polygon class="label-black" points="0,240 746,240 829,47 1028,47 1028,370 0,370" fill="var(--label-black)"/>
  <polygon class="red-stripe" points="0,228 742,228 823,38 1028,38 1028,47 829,47 746,240 0,240" fill="url(#redStripe)"/>

  <!-- brand -->
  <rect x="20" y="32" width="12" height="12" fill="var(--brand-red)"/>
  <text class="brand-name" x="38" y="47" font-size="26">KORVALT</text>

  <!-- product name -->
  <text class="product-name" x="180" y="150" font-size="84" textLength="520" lengthAdjust="spacingAndGlyphs">VOLTMASTRO</text>
  <text class="duty-line" x="700" y="200" font-size="28" text-anchor="end">SUPER HEAVY DUTY</text>

  <!-- specifications table -->
  <g class="spec-table" transform="translate(25 245)">
    <rect x="0" y="0" width="142" height="109" fill="var(--panel-white)"/>
    <rect x="1" y="1" width="140" height="9" fill="var(--label-black)"/>
    <text class="spec-title" x="71" y="9" text-anchor="middle">BATTERY SPECIFICATIONS</text>
    <line x1="56" y1="10" x2="56" y2="108" stroke="#555" stroke-width="0.5"/>
    <g stroke="#555" stroke-width="0.5">
      <line x1="1" y1="20" x2="141" y2="20"/><line x1="1" y1="30" x2="141" y2="30"/>
      <line x1="1" y1="40" x2="141" y2="40"/><line x1="1" y1="50" x2="141" y2="50"/>
      <line x1="1" y1="60" x2="141" y2="60"/><line x1="1" y1="79" x2="141" y2="79"/>
      <line x1="1" y1="89" x2="141" y2="89"/><line x1="1" y1="99" x2="141" y2="99"/>
    </g>
    <g class="spec-cell">
      <text x="28" y="17" text-anchor="middle">Power Output</text><text x="99" y="17" text-anchor="middle">52.1 kW</text>
      <text x="28" y="27" text-anchor="middle">Voltage</text><text x="99" y="27" text-anchor="middle">58 V/116 V</text>
      <text x="28" y="37" text-anchor="middle">Current</text><text x="99" y="37" text-anchor="middle">726 A/363 A</text>
      <text x="28" y="47" text-anchor="middle">Capacity</text><text x="99" y="47" text-anchor="middle">375 kWh</text>
      <text x="28" y="57" text-anchor="middle">Efficiency</text><text x="99" y="57" text-anchor="middle">&gt;83%</text>
      <text x="28" y="67" text-anchor="middle">Dimensions</text><text x="99" y="67" text-anchor="middle">W:2.17 m; D:1.69 m;</text>
      <text x="99" y="76" text-anchor="middle">H:0.64 m</text>
      <text x="28" y="86" text-anchor="middle">Weight</text><text x="99" y="86" text-anchor="middle">3.5 ton</text>
      <text x="28" y="96" text-anchor="middle">Energy Density</text><text x="99" y="96" text-anchor="middle">160 kWh/m³</text>
      <text x="28" y="106" text-anchor="middle">No. of Cells</text><text x="99" y="106" text-anchor="middle">320</text>
    </g>
  </g>

  <!-- tagline -->
  <text class="tagline" x="209" y="322" font-size="33" textLength="496" lengthAdjust="spacingAndGlyphs">THE STEADY CHARGE THAT HOLDS</text>

  <!-- warning panel -->
  <g class="warning-panel">
    <rect x="842" y="61" width="164" height="290" fill="var(--panel-white)"/>
    <circle cx="868" cy="82" r="11" fill="var(--brand-blue)"/>
    <rect x="863" y="76" width="9" height="11" fill="none" stroke="#fff" stroke-width="1.2"/>
    <text class="warning-text" x="889" y="85">Note Operating Instructions</text>

    <circle cx="868" cy="117" r="11" fill="var(--brand-blue)"/>
    <circle cx="868" cy="116" r="4" fill="none" stroke="#fff" stroke-width="1.2"/>
    <text class="warning-text" x="889" y="115">Shield eyes- eye protection</text>
    <text class="warning-text" x="889" y="124">must be worn</text>

    <circle cx="868" cy="150" r="11" fill="#fff" stroke="var(--brand-red)" stroke-width="2"/>
    <line x1="860" y1="142" x2="876" y2="158" stroke="var(--brand-red)" stroke-width="2"/>
    <text class="warning-text" x="889" y="153">Keep away from children</text>

    <polygon points="868,169 880,189 856,189" fill="#f5c400" stroke="var(--label-black)" stroke-width="1"/>
    <text class="warning-text" x="889" y="177">Battery acid - corrosive</text>
    <text class="warning-text" x="889" y="186">and poisonous</text>

    <circle cx="868" cy="208" r="11" fill="#fff" stroke="var(--brand-red)" stroke-width="2"/>
    <line x1="860" y1="200" x2="876" y2="216" stroke="var(--brand-red)" stroke-width="2"/>
    <text class="warning-text" x="889" y="206">No smoking - no naked flames</text>
    <text class="warning-text" x="889" y="215">- no sparks</text>

    <polygon points="868,229 879,247 857,247" fill="#f5c400" stroke="var(--label-black)" stroke-width="1"/>
    <text class="warning-text" x="889" y="241">Explosive gases</text>

    <text class="warning-pb" x="868" y="268" font-size="14" text-anchor="middle">Pb</text>
    <text class="warning-text" x="889" y="265">Contains lead</text>

    <rect x="862" y="279" width="12" height="14" fill="none" stroke="var(--ink)" stroke-width="1"/>
    <line x1="857" y1="277" x2="879" y2="297" stroke="var(--ink)" stroke-width="1"/>
    <line x1="879" y1="277" x2="857" y2="297" stroke="var(--ink)" stroke-width="1"/>
    <text class="warning-pb" x="868" y="305" font-size="7" text-anchor="middle">Pb</text>
    <text class="warning-text" x="889" y="282">Never disposal of as domestic</text>
    <text class="warning-text" x="889" y="291">waste - take to a designated</text>
    <text class="warning-text" x="889" y="300">waste reclamation site</text>

    <circle cx="868" cy="330" r="9" fill="none" stroke="var(--ink)" stroke-width="3" stroke-dasharray="12 4"/>
    <text class="warning-text" x="889" y="322">Battery is recyclable - follow</text>
    <text class="warning-text" x="889" y="331">local recycling &amp; reclaiming</text>
    <text class="warning-text" x="889" y="340">procedures</text>
  </g>
</svg>
</body>
</html>
```